Finance Flyer/ brouchure Design

I would a finance flyer/ brouchure deisgned detailing the services that we offer as per the below.
Lending & Leasing
General Insurance
Risk Insurance
Wealth Planning
Commercial, Equipment & Asset Finance
I would also like the brouchure to state that 'we have access to over 35 lenders', 'Our services are free to you', 'We will find you the best deal & make it easy for you'.
I would like a spot on the flyer/ brouchure where I can place a picture of the local finance broker and a short bio on them.
I would like to be able to come back to the person ultimately chosen to design a suite of flyers.

Target Market(s)

My target auidience are families, aged between 30 & 50 with children.
I would like the flyer to appear professional but friendly and to work with the colours of my logo.

Industry/Entity Type

Finance

Font styles to use
Serif

Colors

Designer to choose colors to be used in the design.

Requirements
Must have
• Be friendly & inviting
• Work with the colours of my logo
• Call to action - 'Call us today on 1300 482 615'
• Must have a Contact us section including the following
• Phone number- 1300 482 615
• Location- Brisbane & surrounds
• Email- Moira@tallowbq.com.au
• Website- www.tallowbq.com.au
• Facebook- www.facebook.com/tallowmonetary

```html
<!DOCTYPE html>
<html lang="en">
<head>
<meta charset="utf-8">
<title>Tallow Financial Solutions – Flyer</title>
<link href="https://fonts.googleapis.com/css2?family=Open+Sans:wght@400;600;700;800&display=swap" rel="stylesheet">
<style>
  :root {
    --bg: #2a2624;
    --teal: #1e5b68;
    --teal-dark: #123f4c;
    --teal-deep: #0b3340;
    --panel: #cfe5f2;
    --panel-text: #1d4a5a;
    --green: #8cc63f;
    --white: #ffffff;
    --photo-top: #dfe6ee;
    --photo-mid: #b9c7d6;
    --photo-warm: #d9c3a3;
  }
  * { margin: 0; padding: 0; box-sizing: border-box; }
  html, body { width: 1200px; height: 1200px; overflow: hidden; }
  body {
    background: var(--bg);
    font-family: "Open Sans", Arial, sans-serif;
    position: relative;
  }
  .flyer {
    position: absolute;
    left: 204px; top: 40px;
    width: 792px; height: 1120px;
    background: var(--teal);
    overflow: hidden;
  }
  .hero-photo {
    position: absolute; left: 0; top: 0;
    width: 792px; height: 640px;
    background: linear-gradient(180deg, var(--photo-top) 0%, var(--photo-mid) 55%, var(--photo-warm) 75%, #6f8091 100%);
  }
  .shapes { position: absolute; left: 0; top: 0; }
  .brand {
    position: absolute; right: 44px; top: 40px;
    display: flex; align-items: center; gap: 12px;
  }
  .brand-mark { width: 26px; height: 26px; background: var(--green); }
  .brand-name {
    font-weight: 800; font-size: 28px; color: var(--teal);
    letter-spacing: 1px; text-transform: uppercase; line-height: 1.05;
  }
  .info-panel {
    position: absolute; left: 370px; top: 390px;
    width: 422px; height: 500px;
    padding: 34px 30px 0 26px;
    color: var(--panel-text);
  }
  .head-unbold { font-size: 21px; font-weight: 400; text-transform: uppercase; line-height: 1.1; }
  .head-bold { font-size: 25px; font-weight: 800; text-transform: uppercase; line-height: 1.15; margin-bottom: 12px; }
  .bio { font-size: 14px; line-height: 1.55; }
  .divider { position: relative; margin: 18px 0 14px; height: 1px; background: var(--panel-text); }
  .divider::before, .divider::after {
    content: ""; position: absolute; top: -3px; width: 7px; height: 7px;
    border-radius: 50%; background: var(--panel-text);
  }
  .divider::before { left: 0; }
  .divider::after { right: 0; }
  .promises { list-style: none; }
  .promises li {
    font-size: 16px; font-weight: 800; line-height: 1.35;
    padding-left: 18px; position: relative; color: var(--teal-deep);
  }
  .promises li::before { content: "•"; position: absolute; left: 0; }
  .broker-photo {
    position: absolute; left: 80px; top: 450px;
    width: 230px; height: 230px;
    border: 7px solid var(--white);
    outline: 4px solid var(--green);
  }
  .broker-photo div {
    width: 100%; height: 100%;
    background: linear-gradient(160deg, #c9b08a 0%, #e9d8c4 50%, #9fb2c4 100%);
  }
  .offer-label {
    position: absolute; left: 60px; top: 718px;
    background: var(--green); color: var(--white);
    font-size: 28px; font-weight: 700; padding: 2px 16px;
  }
  .services {
    position: absolute; left: 62px; top: 774px;
    width: 300px;
    list-style: none; color: var(--white);
  }
  .services li {
    font-size: 19px; font-weight: 700; text-transform: uppercase;
    line-height: 1.32; padding-left: 20px; position: relative;
    white-space: nowrap;
  }
  .services li::before {
    content: ""; position: absolute; left: 0; top: 8px;
    width: 9px; height: 9px; border-radius: 50%; background: var(--green);
  }
  .services li.cont::before { display: none; }
  .contact {
    position: absolute; left: 62px; top: 960px;
    color: var(--white);
  }
  .contact-title {
    font-size: 15px; font-weight: 800; color: var(--green);
    text-transform: uppercase; letter-spacing: 1px; margin-bottom: 4px;
  }
  .contact p { font-size: 13.5px; line-height: 1.5; }
  .contact b { font-weight: 700; color: var(--green); }
  .call-to-action {
    position: absolute; left: 420px; bottom: 56px;
    color: var(--white);
  }
  .cta-lead { font-size: 24px; font-weight: 400; text-transform: uppercase; }
  .cta-phone { font-size: 40px; font-weight: 800; line-height: 1.1; }
</style>
</head>
<body>
  <main class="flyer">
    <div class="hero-photo" role="img" aria-label="Businessman pointing at hand-drawn finance sketches and charts over a city skyline"></div>

    <svg class="shapes" width="792" height="1120" viewBox="0 0 792 1120" aria-hidden="true">
      <polygon points="0,640 370,560 370,1120 0,1120" fill="#1e5b68"/>
      <rect x="370" y="390" width="422" height="500" fill="#cfe5f2"/>
      <rect x="370" y="890" width="422" height="230" fill="#0b3340"/>
      <polygon points="0,950 370,900 370,1120 0,1120" fill="#123f4c"/>
    </svg>

    <div class="brand">
      <span class="brand-mark"></span>
      <span class="brand-name">Tallow<br>Financial Solutions</span>
    </div>

    <section class="info-panel">
      <p class="head-unbold">Head Title Unbold</p>
      <h1 class="head-bold">Main Head Title Bold</h1>
      <p class="bio">Moira has helped Brisbane families find the right loan for over twelve years. She listens first, explains every option in plain words and handles the paperwork so you can focus on home. Whether you are buying your first house, upgrading for a growing family or planning ahead, Moira will compare lenders and guide you through each step with care.</p>
      <div class="divider"></div>
      <ul class="promises">
        <li>We have access to over 35 lenders</li>
        <li>Our services are free to you</li>
        <li>We will find you the best deal &amp; make it easy for you.</li>
      </ul>
    </section>

    <div class="broker-photo"><div role="img" aria-label="Portrait of the local finance broker"></div></div>

    <div class="offer-label">WE OFFER</div>
    <ul class="services">
      <li>Lending &amp; Leasing</li>
      <li>General Insurance</li>
      <li>Risk Insurance</li>
      <li>Wealth Planning</li>
      <li>Commercial, Equipment</li>
      <li class="cont">&amp; Asset Finance</li>
    </ul>

    <section class="contact">
      <h2 class="contact-title">Contact Us</h2>
      <p><b>P</b> 1300 482 615</p>
      <p><b>L</b> Brisbane &amp; surrounds</p>
      <p><b>E</b> Moira@tallowbq.com.au</p>
      <p><b>W</b> www.tallowbq.com.au</p>
      <p><b>F</b> www.facebook.com/tallowmonetary</p>
    </section>

    <div class="call-to-action">
      <p class="cta-lead">Call us today on</p>
      <p class="cta-phone">1300 482 615</p>
    </div>
  </main>
</body>
</html>
```